Sales and Lettings Boards

Hello, please see attached our sales and lettings boards for our estate agency. These were "designed" by the sign writers. As you can see they are pretty flat and boring - could you work your magic and make them stand out please? I've also attached the logo files. Many thanks, Dean

Target Market(s)

Consumers - residential sale property sales and lettings

Industry/Entity Type

Real Estate Agent

```html
<!DOCTYPE html>
<html lang="en">
<head>
<meta charset="utf-8">
<title>Keston Sales &amp; Letting – For Sale Board</title>
<link rel="stylesheet" href="https://fonts.googleapis.com/css2?family=Quicksand:wght@400;500;600;700&display=swap">
<style>
  :root {
    --backdrop: #333333;
    --board-white: #fafafa;
    --brand-green: #4ab832;
    --brand-charcoal: #333333;
    --text-white: #ffffff;
  }
  html, body {
    margin: 0;
    padding: 0;
    width: 1200px;
    height: 1200px;
    overflow: hidden;
    background: var(--backdrop);
  }
  .board {
    display: block;
    width: 1200px;
    height: 1200px;
    font-family: "Quicksand", sans-serif;
  }
  .board-outline { fill: var(--board-white); stroke: var(--brand-green); stroke-width: 14; stroke-linejoin: round; }
  .band-status { fill: var(--brand-green); }
  .band-phone { fill: var(--brand-charcoal); }
  .brand-name { fill: var(--brand-charcoal); font-weight: 700; font-size: 172px; }
  .brand-strapline { fill: var(--brand-charcoal); font-weight: 500; font-size: 62px; }
  .status-label { fill: var(--text-white); font-weight: 500; font-size: 136px; }
  .phone-number { fill: var(--text-white); font-weight: 700; font-size: 88px; }
  .web-address { fill: var(--brand-green); font-weight: 700; font-size: 33px; }
</style>
</head>
<body>
<svg class="board" viewBox="0 0 1200 1200" xmlns="http://www.w3.org/2000/svg" role="img" aria-label="Keston Sales and Letting for sale board">
  <defs>
    <clipPath id="board-body">
      <rect x="250" y="560" width="702" height="464" rx="30"/>
    </clipPath>
  </defs>

  <path class="board-outline"
        d="M590,128 Q600,124 612,134 L1034,500 Q1070,532 1044,568 Q1008,604 990,586 L960,562 L960,996 Q960,1024 932,1024 L272,1024 Q244,1024 244,996 L244,562 L210,592 Q190,606 160,584 Q116,548 150,518 L568,136 Q578,126 590,128 Z"/>

  <g clip-path="url(#board-body)">
    <rect class="band-status" x="250" y="621" width="702" height="205"/>
    <rect class="band-phone" x="250" y="826" width="702" height="126"/>
  </g>

  <text class="brand-name" x="308" y="541" textLength="620" lengthAdjust="spacingAndGlyphs">KESTON</text>
  <text class="brand-strapline" x="398" y="600" textLength="404" lengthAdjust="spacingAndGlyphs">Sales &amp; Letting</text>

  <text class="status-label" x="284" y="768" textLength="640" lengthAdjust="spacingAndGlyphs">FOR SALE</text>
  <text class="phone-number" x="316" y="912" textLength="568" lengthAdjust="spacingAndGlyphs">01632 960418</text>
  <text class="web-address" x="372" y="994" textLength="424" lengthAdjust="spacingAndGlyphs">www.keston-estates.com</text>
</svg>
</body>
</html>
```